Brightmarrow4Pay Pty Ltd
CorporateTelecommunications Auditor & Leakage Expert
Korin Thewel
Managing Director
Unit 8 / 14 Pelham Rd Dunmore Vale VIC 3149
korin.thewel@brightmarrow4pay.com
Your CorporateTelecommunications Auditor & Leakage Expert

```html
<!DOCTYPE html>
<html lang="en">
<head>
<meta charset="utf-8">
<title>Brightmarrow4Pay Stationery</title>
<link href="https://fonts.googleapis.com/css2?family=Open+Sans:wght@400;600;700&display=swap" rel="stylesheet">
<style>
:root{
  --bg:#ece9e4;
  --paper:#ffffff;
  --red:#c8161d;
  --red-dark:#8e0f14;
  --grey:#4a4a4a;
  --grey-light:#b9b9b9;
  --ink:#555555;
  --faint:#f1dede;
}
*{margin:0;padding:0;box-sizing:border-box}
html,body{width:1200px;height:346px;overflow:hidden}
body{background:var(--bg);font-family:"Open Sans",Arial,sans-serif;color:var(--ink);position:relative}
.sheet{position:absolute;background:var(--paper);box-shadow:0 1px 3px rgba(0,0,0,.18)}
.label{position:absolute;font-size:5px;letter-spacing:.5px;text-transform:uppercase;color:#777;white-space:nowrap}
.brand{display:flex;align-items:center;gap:3px;font-weight:700;color:var(--red);white-space:nowrap}
.brand .mark{background:var(--red);display:block}
.brand-sm{font-size:6px}
.brand-sm .mark{width:8px;height:8px}
.tiny{font-size:3.6px;line-height:5px;color:var(--ink)}
.swoosh{position:absolute;left:0;bottom:0;width:100%;display:block}
.faint-name{position:absolute;font-weight:700;color:var(--faint);text-align:center;line-height:1}

/* business cards */
.card-front{left:29px;top:108px;width:115px;height:66px}
.card-front .brand{position:absolute;left:8px;top:8px}
.card-front .details{position:absolute;left:8px;bottom:8px}
.card-front .name{font-size:5px;font-weight:700;color:var(--grey)}
.card-back{left:29px;top:240px;width:115px;height:66px;background:linear-gradient(180deg,var(--red),var(--red-dark));border-radius:4px;display:flex;align-items:center;justify-content:center}
.card-back .brand{color:#fff;font-size:8px}
.card-back .brand .mark{background:#fff;width:10px;height:10px}

/* letterheads */
.letterhead{top:24px;width:190px;height:262px}
.letterhead-1{left:163px}
.letterhead-2{left:372px}
.letterhead .brand{position:absolute;left:14px;top:12px}
.letterhead .address{position:absolute;right:12px;top:12px;text-align:right}
.letterhead .faint-name{left:10px;right:10px;top:120px;font-size:17px}
.letterhead .faint-square{position:absolute;left:75px;top:72px;width:40px;height:40px;background:var(--faint)}

/* compliment slips */
.slip{left:619px;width:185px;height:90px}
.slip-1{top:108px}
.slip-2{top:226px}
.slip .brand{position:absolute;left:12px;top:12px}
.slip .tagline{position:absolute;left:12px;top:26px}

/* envelopes */
.env-back{left:900px;top:108px;width:276px;height:84px;overflow:hidden}
.env-front{left:900px;top:226px;width:276px;height:84px}
.env-front .brand{position:absolute;left:12px;top:10px}
.env-front .address{position:absolute;left:12px;top:22px}
</style>
</head>
<body>

<!-- business card front -->
<div class="sheet card-front">
  <div class="brand brand-sm"><span class="mark"></span>Brightmarrow4Pay</div>
  <div class="details tiny">
    <div class="name">Korin Thewel</div>
    <div>Managing Director</div>
    <div>korin.thewel@brightmarrow4pay.com</div>
    <div>Unit 8 / 14 Pelham Rd Dunmore Vale VIC 3149</div>
  </div>
</div>
<div class="label" style="left:29px;top:99px">Card front</div>

<!-- business card back -->
<div class="sheet card-back">
  <div class="brand"><span class="mark"></span>Brightmarrow4Pay</div>
</div>
<div class="label" style="left:29px;top:231px">Card back</div>

<!-- letterhead 1 -->
<div class="sheet letterhead letterhead-1">
  <div class="brand brand-sm"><span class="mark"></span>Brightmarrow4Pay</div>
  <div class="address tiny">
    <div>Brightmarrow4Pay Pty Ltd</div>
    <div>Unit 8 / 14 Pelham Rd Dunmore Vale VIC 3149</div>
    <div>korin.thewel@brightmarrow4pay.com</div>
  </div>
  <span class="faint-square"></span>
  <div class="faint-name">Brightmarrow4Pay</div>
  <svg class="swoosh" viewBox="0 0 190 14" preserveAspectRatio="none" height="14">
    <polygon points="0,5 110,5 104,14 0,14" fill="var(--red)"/>
    <polygon points="112,5 190,2 190,14 106,14" fill="var(--grey)"/>
  </svg>
</div>
<div class="label" style="left:220px;top:290px">Letterhead page one</div>

<!-- letterhead 2 -->
<div class="sheet letterhead letterhead-2">
  <div class="brand brand-sm"><span class="mark"></span>Brightmarrow4Pay</div>
  <span class="faint-square"></span>
  <div class="faint-name">Brightmarrow4Pay</div>
  <svg class="swoosh" viewBox="0 0 190 14" preserveAspectRatio="none" height="14">
    <polygon points="0,5 110,5 104,14 0,14" fill="var(--red)"/>
    <polygon points="112,5 190,2 190,14 106,14" fill="var(--grey)"/>
  </svg>
</div>
<div class="label" style="left:430px;top:290px">Letterhead page two</div>

<!-- compliment slips -->
<div class="sheet slip slip-1">
  <div class="brand brand-sm"><span class="mark"></span>Brightmarrow4Pay</div>
  <div class="tagline tiny">Your CorporateTelecommunications Auditor &amp; Leakage Expert</div>
  <svg class="swoosh" viewBox="0 0 185 10" preserveAspectRatio="none" height="10">
    <polygon points="0,4 105,4 99,10 0,10" fill="var(--red)"/>
    <polygon points="107,4 185,1 185,10 101,10" fill="var(--grey)"/>
  </svg>
</div>
<div class="label" style="left:680px;top:201px">Compliment slip</div>

<div class="sheet slip slip-2">
  <div class="brand brand-sm"><span class="mark"></span>Brightmarrow4Pay</div>
  <div class="tagline tiny">Your CorporateTelecommunications Auditor &amp; Leakage Expert</div>
  <svg class="swoosh" viewBox="0 0 185 10" preserveAspectRatio="none" height="10">
    <polygon points="0,4 105,4 99,10 0,10" fill="var(--red)"/>
    <polygon points="107,4 185,1 185,10 101,10" fill="var(--grey)"/>
  </svg>
</div>
<div class="label" style="left:680px;top:319px">Compliment slip</div>

<!-- envelope back -->
<div class="sheet env-back">
  <svg viewBox="0 0 276 84" width="276" height="84" style="display:block">
    <rect width="276" height="84" fill="var(--paper)"/>
    <rect width="276" height="16" fill="var(--red)"/>
    <path d="M0,16 L138,52 L276,16 Z" fill="var(--grey)"/>
    <path d="M0,84 L138,46 L276,84" fill="none" stroke="#e2e2e2" stroke-width="1"/>
  </svg>
</div>

<!-- envelope front -->
<div class="sheet env-front">
  <div class="brand brand-sm"><span class="mark"></span>Brightmarrow4Pay</div>
  <div class="address tiny">
    <div>Unit 8 / 14 Pelham Rd Dunmore Vale VIC 3149</div>
  </div>
  <svg class="swoosh" viewBox="0 0 276 8" preserveAspectRatio="none" height="8">
    <polygon points="0,3 160,3 155,8 0,8" fill="var(--red)"/>
    <polygon points="162,3 276,1 276,8 157,8" fill="var(--grey)"/>
  </svg>
</div>
<div class="label" style="left:990px;top:314px">Envelope back and front</div>

</body>
</html>
```